Business card for Sports Apparel business

DOUBLE SIDED DESIGN
We need business cards for a new sports apparel business. We are developing a protective headband for soccer initially.
Quorvane is focused on designing and developing head protection products to reduce the likelihood of concussion when playing sports. Exploring and understanding medical insights, material science research, current and former players experiences and governing bodies guidelines has allowed Quorvane to develop the safety, style, form and function requirements of a suitable product to bring to market.
Target Market(s)
Mums buying kits for the sons and daughters. Amateur footballers.
Industry/Entity Type
Sporting Good
Contact Information for Business Card
Martin Ellwood - CEO
Mobile: +44 7700123456
Email: martin@quorvane.co.uk
Tel: 0208 1234567
Rosalind Pyke - COO
Mob: +44 7700 654321
Email: rosalind@quorvane.co.uk
Tel: 0208 1234567
Gordon Haley - CCO
Mob: +44 7700 987654
Email: gordon@quorvane.co.uk
Tel: 0208 1234567
Look and feel
Each slider illustrates characteristics of the customer's brand and the style your logo design should communicate.

```html
<!DOCTYPE html>
<html lang="en">
<head>
<meta charset="utf-8">
<title>Quorvane business card</title>
<link rel="stylesheet" href="https://fonts.googleapis.com/css2?family=Montserrat:wght@400;500;700&display=swap">
<style>
  :root {
    --stage: #2a2a2a;
    --grey: #666666;
    --blue: #135f93;
    --white: #ffffff;
    --ink: #6a6a6a;
  }
  html, body {
    margin: 0;
    padding: 0;
    width: 1200px;
    height: 900px;
    overflow: hidden;
    background: var(--stage);
    font-family: "Montserrat", sans-serif;
  }
  .card {
    position: absolute;
    left: 250px;
    width: 700px;
    height: 400px;
    background: var(--white);
    overflow: hidden;
  }
  .card--front { top: 35px; }
  .card--back { top: 465px; }

  /* front side */
  .front__grey {
    position: absolute;
    left: 0; top: 28px; bottom: 0;
    width: 300px;
    background: var(--grey);
  }
  .front__blue {
    position: absolute;
    left: 360px; top: 28px; right: 0; bottom: 28px;
    background: var(--blue);
  }
  .front__name {
    position: absolute;
    left: 360px; right: 0; top: 28px; bottom: 28px;
    display: flex;
    align-items: center;
    justify-content: center;
    color: var(--white);
    font-weight: 700;
    font-size: 40px;
    letter-spacing: 6px;
  }

  /* back side */
  .back__panel {
    position: absolute;
    left: 0; top: 0; bottom: 0;
    width: 262px;
    background: var(--grey);
  }
  .back__stripe {
    position: absolute;
    left: 272px; top: 0; bottom: 0;
    width: 9px;
    background: var(--blue);
  }
  .back__brand {
    position: absolute;
    left: 131px; top: 200px;
    transform: translate(-50%, -50%) rotate(-90deg);
    color: var(--white);
    font-weight: 500;
    font-size: 48px;
    letter-spacing: 4px;
    white-space: nowrap;
  }
  .contact {
    position: absolute;
    left: 355px; top: 150px;
  }
  .contact__name {
    margin: 0;
    color: var(--blue);
    font-weight: 700;
    font-size: 21px;
    letter-spacing: 1.5px;
    text-transform: uppercase;
  }
  .contact__role {
    margin: 0 0 20px;
    color: var(--ink);
    font-size: 16px;
  }
  .contact__list {
    list-style: none;
    margin: 0;
    padding: 0;
  }
  .contact__item {
    display: flex;
    align-items: center;
    gap: 12px;
    color: var(--ink);
    font-size: 18px;
    line-height: 27px;
  }
  .contact__icon {
    width: 16px;
    height: 16px;
    flex: none;
  }
</style>
</head>
<body>

<section class="card card--front" aria-label="Card front">
  <div class="front__grey"></div>
  <div class="front__blue"></div>
  <div class="front__name">QUORVANE</div>
</section>

<section class="card card--back" aria-label="Card back">
  <div class="back__panel">
    <div class="back__brand">QUORVANE</div>
  </div>
  <div class="back__stripe"></div>

  <div class="contact">
    <p class="contact__name">Martin Ellwood</p>
    <p class="contact__role">CEO</p>
    <ul class="contact__list">
      <li class="contact__item">
        <svg class="contact__icon" viewBox="0 0 16 16" aria-hidden="true">
          <rect x="4" y="1" width="8" height="14" rx="1.5" fill="none" stroke="#135f93" stroke-width="1.4"/>
          <line x1="7" y1="12.5" x2="9" y2="12.5" stroke="#135f93" stroke-width="1.4"/>
        </svg>
        0208 123 4567
      </li>
      <li class="contact__item">
        <svg class="contact__icon" viewBox="0 0 16 16" aria-hidden="true">
          <path d="M3 2 L6 2 L7 5 L5.5 6.5 Q7 9.5 9.5 10.5 L11 9 L14 10 L14 13 Q8 14 4 9 Q2 6 3 2 Z" fill="none" stroke="#135f93" stroke-width="1.3" stroke-linejoin="round"/>
        </svg>
        +44 7700123456
      </li>
      <li class="contact__item">
        <svg class="contact__icon" viewBox="0 0 16 16" aria-hidden="true">
          <rect x="1" y="3.5" width="14" height="9" fill="none" stroke="#135f93" stroke-width="1.3"/>
          <polyline points="1,3.5 8,9 15,3.5" fill="none" stroke="#135f93" stroke-width="1.3"/>
        </svg>
        martin@quorvane.co.uk
      </li>
    </ul>
  </div>
</section>

</body>
</html>
```